Velumi Organics Natural baby skin and hair care

We need a look and feel for a line of baby care products. A lotion, Wash and baby oil. We already have an existing line of products and are now venturing into baby care. We want a natural look with "love, softness and a touch of earth and Africa'

Industry/Entity Type

Retail

Font styles to use
Script

Colors
fbed22
f78f20
9bcb3c

Requirements
Must have
• Natural elements
Should not have
• Red, Black abstract shapes

```html
<!DOCTYPE html>
<html lang="en">
<head>
<meta charset="utf-8">
<title>Velumi Baby Oil – Label</title>
<link rel="stylesheet" href="https://fonts.googleapis.com/css2?family=Fredoka:wght@400;600&family=Patrick+Hand&family=Patrick+Hand+SC&family=Sriracha&family=Dancing+Script:wght@700&display=swap">
<style>
  :root {
    --backdrop: #eeeef1;
    --lime: #a9d03c;
    --lime-light: #c2e264;
    --lime-cloud: #bfe060;
    --leaf-dark: #1e7a34;
    --band-green: #1f7f37;
    --cap-green: #1c5a2b;
    --cap-shadow: #123f1d;
    --crimp: #b6da48;
    --white: #ffffff;
  }
  html, body {
    margin: 0;
    width: 1200px;
    height: 1200px;
    overflow: hidden;
    background: var(--backdrop);
  }
  .label-art { display: block; width: 1200px; height: 1200px; }
  .tube-body { fill: url(#bodyShade); }
  .tube-crimp { fill: var(--crimp); }
  .crimp-lines { stroke: #98c236; stroke-width: 2; }
  .volume-band { fill: var(--band-green); }
  .cap { fill: var(--cap-green); }
  .cap-lid { fill: none; stroke: var(--cap-shadow); stroke-width: 3; }
  .floral-border { fill: #8cbf33; opacity: .75; }
  .cloud { fill: var(--lime-cloud); stroke: var(--leaf-dark); stroke-width: 3; }
  .brand-frame { fill: none; stroke: var(--white); stroke-width: 2; }
  .claim { font-family: "Patrick Hand", sans-serif; font-size: 36px; fill: var(--leaf-dark); letter-spacing: 1.5px; }
  .brand-name { font-family: "Fredoka", sans-serif; font-weight: 400; font-size: 23px; fill: var(--white); letter-spacing: 2px; }
  .product-script { font-family: "Dancing Script", cursive; font-weight: 700; font-size: 60px; fill: var(--band-green); }
  .product-name { font-family: "Fredoka", sans-serif; font-weight: 600; font-size: 56px; fill: var(--leaf-dark); }
  .ingredients { font-family: "Sriracha", cursive; font-size: 17px; fill: var(--band-green); }
  .tagline { font-family: "Patrick Hand SC", sans-serif; font-size: 23px; fill: var(--band-green); }
  .volume { font-family: "Patrick Hand", sans-serif; font-size: 24px; fill: var(--white); letter-spacing: 1.5px; }
</style>
</head>
<body>
<svg class="label-art" viewBox="0 0 1200 1200" xmlns="http://www.w3.org/2000/svg">
  <defs>
    <linearGradient id="bodyShade" x1="0" x2="1" y1="0" y2="0">
      <stop offset="0" stop-color="#96c232"/>
      <stop offset=".4" stop-color="var(--lime-light)"/>
      <stop offset=".7" stop-color="var(--lime)"/>
      <stop offset="1" stop-color="#8fbb2e"/>
    </linearGradient>
    <clipPath id="bodyClip">
      <path d="M388 112 H812 L742 958 H458 Z"/>
    </clipPath>
  </defs>

  <!-- tube crimp -->
  <rect class="tube-crimp" x="386" y="80" width="428" height="34" rx="3"/>
  <g class="crimp-lines">
    <line x1="386" y1="90" x2="814" y2="90"/>
    <line x1="386" y1="100" x2="814" y2="100"/>
  </g>

  <!-- tube body -->
  <path class="tube-body" d="M388 112 H812 L742 958 H458 Z"/>

  <g clip-path="url(#bodyClip)">
    <!-- floral side borders -->
    <path class="floral-border" role="img" aria-label="Hand-drawn flowers and leaves along the left edge" d="M395 200 q40 40 30 120 q-10 80 25 130 q20 60 -10 120 l-60 0 z"/>
    <path class="floral-border" role="img" aria-label="Hand-drawn flowers and leaves along the right edge" d="M805 200 q-40 40 -30 120 q10 80 -25 130 q-20 60 10 120 l60 0 z"/>

    <!-- volume band -->
    <rect class="volume-band" x="380" y="880" width="440" height="80"/>
  </g>

  <text class="claim" x="600" y="173" text-anchor="middle">100% NATURAL</text>

  <!-- brand block -->
  <rect class="brand-frame" x="486" y="226" width="218" height="222"/>
  <rect class="brand-frame" x="494" y="234" width="202" height="206"/>
  <text class="brand-name" x="595" y="338" text-anchor="middle">Velumi Organics</text>

  <!-- cloud -->
  <path class="cloud" d="M480 565 A60 60 0 0 1 545 512 A80 80 0 0 1 655 512 A55 55 0 0 1 715 558 A60 60 0 0 1 732 640 A60 60 0 0 1 705 718 A60 60 0 0 1 640 765 A60 60 0 0 1 560 765 A60 60 0 0 1 497 718 A60 60 0 0 1 468 640 A55 55 0 0 1 480 565 Z"/>

  <text class="product-script" x="600" y="585" text-anchor="middle">Velumi</text>
  <text class="product-name" x="600" y="653" text-anchor="middle">BABY OIL</text>
  <text class="ingredients" x="600" y="695" text-anchor="middle">Pure Shea Oil, &amp; Marula Oil</text>
  <text class="ingredients" x="600" y="719" text-anchor="middle">with Myrrh &amp; Frankinsense</text>

  <!-- tagline -->
  <text class="tagline" x="600" y="840" text-anchor="middle" textLength="280" lengthAdjust="spacingAndGlyphs">NURTURE, MOISTURISE, PROTECT</text>

  <text class="volume" x="600" y="920" text-anchor="middle">250ML/8OZ.</text>

  <!-- cap -->
  <rect class="cap" x="474" y="958" width="252" height="158" rx="8"/>
  <path class="cap-lid" d="M522 1040 H678 V1000 H522 Z"/>
</svg>
</body>
</html>
```